Postcard Design

Dentist Office trying to attract new patients
11" x 6" Print Size ("Postcard template" on brief is not required)

Target Market(s)

Moms with kids, Families, Everybody

Industry/Entity Type

Office

Requirements
Must have
• Postage requirements or template are not required in this project. Please use the following guidelines instead.

(11" x 6") Print Size
Requirements for QTRV Retail Indicia (attached file)
* Place the QTRV Retail Indicia in the upper right hand corner of the mail piece.
* Leave 1/8" space from top and right edge.
* Should fit in the area 1.625" from the right edge and 1.375" from top edge.
* No specific size requirement, but must be larger than .5" x .5".
* Font must be in all caps and minimum 4 point size.

The design should focus on quality, comfort and convenience of a dental office. check out the website www.lowvaleteeth.com for ideas.
Include:
-Accepting most PPO Insurance plans
-Evening and Saturday appointments available
- New Patient Specials ...
*Using the logo is optional.

```html
<!DOCTYPE html>
<html lang="en">
<head>
<meta charset="utf-8">
<title>Lowvale Family and Cosmetic Dentistry – Postcard</title>
<link rel="stylesheet" href="https://fonts.googleapis.com/css2?family=Lora:ital,wght@0,400;0,600;1,400;1,600&display=swap">
<style>
  :root {
    --bg: #e9ecef;
    --blue: #25a9d6;
    --blue-deep: #1592c0;
    --blue-text: #1d9fd0;
    --teal-text: #2a8fb0;
    --white: #ffffff;
    --photo-light: #eef0f2;
    --photo-mid: #8d99a2;
    --ink: #2b2b2b;
  }
  * { box-sizing: border-box; margin: 0; padding: 0; }
  html, body { width: 1200px; height: 675px; overflow: hidden; background: var(--bg); }
  body { position: relative; font-family: "Lora", Georgia, serif; }

  .card-slot { position: absolute; top: 182px; width: 572px; height: 312px; }
  .card-slot--front { left: 20px; }
  .card-slot--back { left: 608px; }
  .card {
    width: 1100px; height: 600px; position: relative; overflow: hidden;
    transform: scale(0.52); transform-origin: top left;
    background: var(--white); box-shadow: 0 6px 24px rgba(0,0,0,.25);
  }

  /* Front */
  .front-photo {
    position: absolute; inset: 0;
    background: linear-gradient(100deg, var(--photo-light) 0%, #f6f7f8 18%, #b7c0c6 34%, var(--photo-mid) 50%, #7f8b94 60%, #c6ccd0 100%);
  }
  .front-panel { position: absolute; inset: 0; }
  .front-quote {
    position: absolute; left: 370px; top: 140px; width: 250px;
    color: var(--white); font-style: italic; font-size: 24px; line-height: 1.3;
    text-shadow: 0 1px 4px rgba(0,0,0,.45);
  }
  .front-tagline {
    position: absolute; left: 40px; bottom: 75px;
    color: var(--blue-text); font-style: italic; font-size: 44px;
  }
  .brand {
    position: absolute; left: 640px; top: 60px; display: flex; align-items: center; gap: 16px;
    color: var(--white); font-style: italic; font-size: 34px; line-height: 1.05;
  }
  .brand__dot { width: 46px; height: 46px; border-radius: 50%; background: var(--white); flex: none; }
  .brand__sub { display: block; font-size: 26px; padding-left: 40px; }
  .front-benefits { position: absolute; left: 660px; top: 220px; list-style: none; color: var(--white); }
  .front-benefits li { position: relative; padding-left: 34px; font-size: 31px; line-height: 1.1; margin-bottom: 34px; }
  .front-benefits li::before {
    content: ""; position: absolute; left: 0; top: 14px; width: 12px; height: 12px;
    border-radius: 50%; background: var(--white);
  }
  .front-contact { position: absolute; left: 690px; top: 450px; color: var(--white); font-size: 23px; }
  .front-contact p { display: flex; align-items: center; gap: 18px; margin-bottom: 32px; }
  .front-contact svg { width: 30px; height: 30px; flex: none; }

  /* Back */
  .back-photo {
    position: absolute; right: 0; top: 0; width: 560px; height: 600px;
    background: linear-gradient(90deg, rgba(255,255,255,1) 0%, #d6eef7 35%, #b9e0ef 100%);
  }
  .back-copy { position: absolute; left: 40px; top: 22px; width: 440px; color: var(--teal-text); font-size: 13px; line-height: 1.3; }
  .back-copy h2 { font-size: 30px; font-weight: 600; color: var(--blue-text); line-height: 1.1; margin-bottom: 4px; }
  .back-copy h3 { font-size: 24px; font-weight: 400; color: var(--teal-text); margin: 16px 0 6px; }
  .specials { display: flex; gap: 24px; }
  .specials__col { width: 208px; }
  .special-badge { width: 110px; height: 50px; border: 2px solid var(--blue); background: #dff3fa; margin-top: 8px; }
  .doctor { display: flex; gap: 12px; }
  .doctor__portrait { width: 110px; height: 62px; flex: none; background: linear-gradient(#c9d3da, #8c9aa5); }
  .credentials { margin-top: 14px; list-style: none; }
  .back-brand {
    position: absolute; left: 560px; top: 235px; display: flex; align-items: center; gap: 12px;
    color: var(--ink); font-size: 28px; line-height: 1.05;
  }
  .back-brand__dot { width: 34px; height: 34px; border-radius: 50%; background: var(--ink); flex: none; }
  .back-brand__sub { display: block; font-size: 22px; padding-left: 30px; }
  .back-web { position: absolute; left: 0; right: 0; bottom: 30px; text-align: center; color: var(--teal-text); font-size: 24px; letter-spacing: 1px; padding-left: 400px; }
  .indicia {
    position: absolute; top: 13px; right: 13px; width: 150px; padding: 8px 4px;
    border: 2px solid var(--ink); color: var(--ink); text-align: center;
    font-size: 13px; line-height: 1.25; text-transform: uppercase; background: var(--white);
  }
</style>
</head>
<body>

<div class="card-slot card-slot--front">
  <section class="card card--front">
    <div class="front-photo" role="img" aria-label="Photo of a smiling young woman in a dental chair with a bright dental office behind her"></div>
    <svg class="front-panel" viewBox="0 0 1100 600" aria-hidden="true">
      <path d="M560 0 L1100 0 L1100 600 L620 600 C690 480 700 300 620 150 C600 100 580 50 560 0 Z" fill="var(--blue)"/>
      <path d="M660 420 L1100 400 L1100 600 L620 600 C640 540 655 480 660 420 Z" fill="var(--blue-deep)"/>
    </svg>
    <p class="front-quote">"When you visit our office you will know from the moment you walk in that we take pride in providing you with exceptional patient care in a comfortable caring environment."</p>
    <p class="front-tagline">We want to see you smile :)</p>
    <div class="brand">
      <span class="brand__dot"></span>
      <span>Lowvale Family<span class="brand__sub">and Cosmetic Dentistry</span></span>
    </div>
    <ul class="front-benefits">
      <li>Evening and Saturday<br>appointments available</li>
      <li>Accepting most PPO<br>Insurance plans</li>
    </ul>
    <div class="front-contact">
      <p>
        <svg viewBox="0 0 30 30"><circle cx="15" cy="15" r="14" fill="var(--white)"/><text x="15" y="21" text-anchor="middle" font-size="18" fill="var(--blue)" font-family="Lora, serif">@</text></svg>
        hello@lowvaleteeth.com
      </p>
      <p>
        <svg viewBox="0 0 30 30"><circle cx="15" cy="15" r="14" fill="var(--white)"/><path d="M10 8 l3 0 l1.5 4 l-2 1.5 c1 2.2 2.5 3.7 4.5 4.5 l1.5 -2 l4 1.5 l0 3 c-7 1 -13 -5 -12.5 -12.5 z" fill="var(--blue)"/></svg>
        (512) 555-0148
      </p>
    </div>
  </section>
</div>

<div class="card-slot card-slot--back">
  <section class="card card--back">
    <div class="back-photo" role="img" aria-label="Faded light blue photo of a smiling woman"></div>
    <div class="back-copy">
      <h2>New Patient Specials:</h2>
      <div class="specials">
        <div class="specials__col">
          <p>With PPO Insurance<br>Free Exam, X-rays<br>Free Cleaning<br>Free Whitening or Free Brightline Power Toothbrush</p>
          <div class="special-badge" role="img" aria-label="Offer graphic"></div>
        </div>
        <div class="specials__col">
          <p>Without Insurance:<br>$69 Exam, X-Rays<br>$89 Exam, X-Rays, Cleaning, Whitening<br>$99 Exam, X-Rays, Cleaning, Brightline Power Toothbrush<br>10% Off All Procedures</p>
        </div>
      </div>
      <h3>Meet Dr. R (Renwick)</h3>
      <div class="doctor">
        <div class="doctor__portrait" role="img" aria-label="Portrait of the dentist"></div>
        <p>Dr. R received his DDS degree from Westfield University. Since 2002, he has helped thousands of patients with his many years of experience and caring personality.</p>
      </div>
      <ul class="credentials">
        <li>Graduated from Westfield University</li>
        <li>National Dental Board 97th percentile</li>
        <li>Graduated from Northgate Implant Institute</li>
        <li>Fellow member of IAOI - Implant Academy</li>
        <li>Sustaining member of CSD - Cosmetic Smile Society</li>
        <li>Clear aligner certificate holder</li>
        <li>Nitrous Oxide sedation certificate</li>
        <li>Member of Riverbend Dental Society</li>
        <li>Member of Lone Valley Dental Guild</li>
        <li>Member of National Dental Circle</li>
      </ul>
    </div>
    <div class="back-brand">
      <span class="back-brand__dot"></span>
      <span>Lowvale Family<span class="back-brand__sub">and Cosmetic Dentistry</span></span>
    </div>
    <p class="back-web">http://www.lowvaleteeth.com/</p>
    <div class="indicia">PRSRT STD<br>ECRWSS<br>U.S. Postage<br>Paid<br>QTRV Retail</div>
  </section>
</div>

</body>
</html>
```